Brightwave Business Card

Professional Business Card Design required using the attached contact information.

Contact information can be rearranged as required.

The company is a new start up venture developing solar systems, the branding should be in keeping with that of one of the investors whose website is as follows https://www.quorvex.com/

```html
<!DOCTYPE html>
<html lang="en">
<head>
<meta charset="utf-8">
<title>Brightwave Renewables – Business Card</title>
<link href="https://fonts.googleapis.com/css2?family=Montserrat:wght@500;600&family=Roboto:wght@400;500&display=swap" rel="stylesheet">
<style>
  :root {
    --backdrop: #ececec;
    --card-white: #ffffff;
    --brand-green: #2b7260;
    --name-green: #1f6a52;
    --ink: #2a2a2a;
    --ink-dark: #1b1b1b;
  }
  * { margin: 0; padding: 0; box-sizing: border-box; }
  html, body {
    width: 1200px; height: 800px; overflow: hidden;
    background: var(--backdrop);
  }
  .canvas { position: relative; width: 1200px; height: 800px; }

  .card {
    position: absolute;
    width: 571px; height: 328px;
    box-shadow: 0 2px 6px rgba(0,0,0,0.12);
  }
  .card--front {
    left: 475px; top: 32px;
    background: var(--card-white);
  }
  .card--back {
    left: 170px; top: 406px;
    background: var(--brand-green);
    display: flex; align-items: center; justify-content: center;
  }

  .wordmark {
    font-family: "Montserrat", sans-serif;
    font-weight: 600;
    font-size: 20px;
    letter-spacing: 1.6px;
    white-space: nowrap;
  }
  .card--front .wordmark {
    position: absolute; left: 0; right: 0; top: 62px;
    text-align: center;
    color: var(--ink-dark);
  }
  .card--back .wordmark { color: var(--card-white); margin-top: -6px; }

  .contact {
    position: absolute; left: 41px; top: 144px;
    font-family: "Roboto", sans-serif;
    color: var(--ink);
  }
  .contact__name {
    font-family: "Montserrat", sans-serif;
    font-weight: 500;
    font-size: 18px;
    letter-spacing: 0.6px;
    color: var(--name-green);
    line-height: 22px;
  }
  .contact__title {
    font-size: 13.5px; font-weight: 500;
    line-height: 18px; margin-top: 1px;
  }
  .contact__company {
    font-size: 14px; color: var(--name-green);
    line-height: 19px; margin-top: 10px;
  }
  .contact__address { font-size: 14px; line-height: 19px; }
  .contact__list { list-style: none; margin-top: 4px; }
  .contact__item {
    display: flex; align-items: center;
    font-size: 14px; line-height: 19px;
  }
  .contact__icon {
    width: 12px; height: 12px; margin-right: 6px;
    fill: var(--name-green); flex: none;
  }
</style>
</head>
<body>
<main class="canvas">
  <section class="card card--front" aria-label="Business card front">
    <div class="wordmark">BRIGHTWAVE RENEWABLES</div>
    <div class="contact">
      <div class="contact__name">DANIEL CORWIN</div>
      <div class="contact__title">Managing Director</div>
      <div class="contact__company">Brightwave Renewables LLC</div>
      <div class="contact__address">218 Harbor Street, Boston, MA 02110</div>
      <ul class="contact__list">
        <li class="contact__item">
          <svg class="contact__icon" viewBox="0 0 24 24" aria-hidden="true"><path d="M6.6 10.8a15.1 15.1 0 0 0 6.6 6.6l2.2-2.2c.3-.3.7-.4 1-.2 1.1.4 2.3.6 3.6.6.6 0 1 .4 1 1V20c0 .6-.4 1-1 1A17 17 0 0 1 3 4c0-.6.4-1 1-1h3.5c.6 0 1 .4 1 1 0 1.3.2 2.5.6 3.6.1.3 0 .7-.2 1z"/></svg>
          +1 (555) 014-2270
        </li>
        <li class="contact__item">
          <svg class="contact__icon" viewBox="0 0 24 24" aria-hidden="true"><path d="M2 5h20v14H2z M2 5l10 8 10-8" fill="none" stroke="currentColor"/><path d="M2 5h20v2l-10 7L2 7z"/><path d="M2 8.5l10 7 10-7V19H2z"/></svg>
          daniel.corwin@brightwave-renewables.com
        </li>
        <li class="contact__item">
          <svg class="contact__icon" viewBox="0 0 24 24" aria-hidden="true"><path d="M12 2a10 10 0 1 0 0 20 10 10 0 0 0 0-20zm-1 17.9A8 8 0 0 1 4.2 10.2L9 15v1a2 2 0 0 0 2 2zm6.9-2.5A2 2 0 0 0 16 16h-1v-3a1 1 0 0 0-1-1H8v-2h2a1 1 0 0 0 1-1V7h2a2 2 0 0 0 2-2v-.4a8 8 0 0 1 2.9 12.8z"/></svg>
          www.quorvex.com
        </li>
      </ul>
    </div>
  </section>

  <section class="card card--back" aria-label="Business card back">
    <div class="wordmark">BRIGHTWAVE RENEWABLES</div>
  </section>
</main>
</body>
</html>
```